design a construction company business card

Design business card around our logo. Card must have all the typical info: name, title, address, phone, email, business name, etc. Somewhere on the card I would like to see our motto "Grounded in honesty... Driven by dedication." Consider adding a splash of bright orange to the card to complement the blues and silvers/grays in the logo. We are open to metallic inks, textures, etc. We would like to see options on both light and dark backgrounds. The font in the logo is Euro Technic Extended Regular.

```html
<!DOCTYPE html>
<html lang="en">
<head>
<meta charset="utf-8">
<title>Halden Contracting – Business Card</title>
<link rel="stylesheet" href="https://fonts.googleapis.com/css2?family=Michroma&family=Krona+One&display=swap">
<style>
  :root {
    --page-bg: #f3f3f3;
    --card-black: #0b0b0b;
    --card-white: #ffffff;
    --brand-blue: #2a62c9;
    --motto-gray: #6d6d6d;
    --faint-gray: #d4d4d4;
    --ink: #111111;
  }
  * { margin: 0; padding: 0; box-sizing: border-box; }
  html, body {
    width: 1200px; height: 1200px; overflow: hidden;
    background: var(--page-bg);
    font-family: "Michroma", sans-serif;
  }
  .card {
    position: absolute;
    left: 222px;
    width: 755px;
    height: 424px;
    border-radius: 36px;
    background: var(--card-black);
    overflow: hidden;
  }
  .card--front { top: 131px; }
  .card--back { top: 608px; }

  .front-brand {
    position: absolute;
    top: 172px; left: 0; right: 0;
    display: flex; justify-content: center; align-items: center; gap: 14px;
    color: var(--brand-blue);
    font-size: 27px;
    letter-spacing: 1px;
  }
  .brand-square {
    width: 20px; height: 20px;
    background: var(--brand-blue);
  }
  .motto {
    position: absolute;
    top: 360px; left: 0; right: 0;
    text-align: center;
    color: var(--motto-gray);
    font-size: 16.5px;
  }

  .back-panel {
    position: absolute;
    top: 48px; left: 0; right: 0;
    height: 328px;
    background: var(--card-white);
    text-align: center;
    color: var(--ink);
  }
  .holder-name {
    position: absolute; top: 20px; left: 0; right: 0;
    font-family: "Krona One", sans-serif;
    font-weight: 400;
    font-size: 19px;
    line-height: 24px;
  }
  .holder-title {
    position: absolute; top: 50px; left: 0; right: 0;
    font-size: 10.5px;
  }
  .back-brand {
    position: absolute; top: 140px; left: 0; right: 0;
    color: var(--faint-gray);
    font-size: 27px;
    letter-spacing: 1px;
  }
  .contact {
    position: absolute; top: 236px; left: 0; right: 0;
    list-style: none;
    font-size: 12px;
    line-height: 19px;
  }
</style>
</head>
<body>
  <section class="card card--front">
    <div class="front-brand"><span class="brand-square"></span><span>HALDEN CONTRACTING, INC.</span></div>
    <p class="motto">Grounded in honesty... Driven by dedication</p>
  </section>

  <section class="card card--back">
    <div class="back-panel">
      <h1 class="holder-name">MAREN CASTELL</h1>
      <p class="holder-title">PROJECT ENGINEER</p>
      <div class="back-brand">HALDEN CONTRACTING, INC.</div>
      <ul class="contact">
        <li>12 ridge line road, suite 740</li>
        <li>+00 555 010 2040</li>
        <li>info@haldenbuild.com</li>
        <li>www.haldenbuild.com</li>
      </ul>
    </div>
  </section>
</body>
</html>
```